Healthy Food Healthy Brain Rack Card

We want a new 2 page (front and page) 3.67" x 8.5" rack card. This rack card is the first of a series we are creating. We will have five more eventually.

The minimum font size for the text on the front is 11 point and also for other main body text.

Use the text on the word document.

The images and layout in the word document are just sample ideas we had.

We have a subscripton to adobe stock images so prefer to get images from there or free high quality images.

The document is for older readers. Do not put text over graphics and keep it simple and easy to read with high contrast.

We are open to any color scheme, though something that conveys fresh and healthy, is good.

We want some very simple design element(s) incorporated that convey Native American communities or heritage. But NO head dress, teepee graphics, etc.

At the top, of the first page we would like a collage of healthy food images. This can include fish, chicken, fresh vegetables, berries, brown rice, etc.

On the back side, the text below the brown box on the word document with the title "mock up" can be smaller as needed.

Please remember to include the funding statement - it can be in a very small font 6/7 point.

For more information about our project, please visit https://velmorcollective.org/mind-care/

```html
<!DOCTYPE html>
<html lang="en">
<head>
<meta charset="utf-8">
<title>Healthy Food, Healthy Brain – Rack Card</title>
<link rel="stylesheet" href="https://fonts.googleapis.com/css2?family=Raleway:wght@500;600;700&family=Mulish:wght@400;600;700&display=swap">
<style>
  :root{
    --page:#ececec;
    --card:#ffffff;
    --teal:#4aa3ab;
    --brick:#b0504a;
    --ink:#1e1e1e;
    --rule:#4aa3ab;
  }
  *{box-sizing:border-box;margin:0;padding:0}
  html,body{width:1200px;height:794px;overflow:hidden;background:var(--page)}
  body{position:relative;font-family:"Mulish",sans-serif;color:var(--ink)}

  .card{position:absolute;top:85px;width:284px;height:619px;background:var(--card);
        box-shadow:0 6px 18px rgba(0,0,0,.12);overflow:hidden}
  .card--front{left:257px}
  .card--back{left:612px}
  .abs{position:absolute}
  .center{text-align:center}

  /* front */
  .collage{left:16px;top:14px;width:252px;height:172px}
  .collage .tile{position:absolute}
  .tile--salmon{left:0;top:0;width:124px;height:84px;background:linear-gradient(135deg,#3a3a3a,#c76a43 55%,#7d2a22)}
  .tile--produce{left:128px;top:0;width:124px;height:84px;background:linear-gradient(135deg,#6a8d3a,#e0a040 50%,#c7462f)}
  .tile--berries{left:0;top:88px;width:124px;height:84px;background:linear-gradient(135deg,#2e3a3f,#b3263a 55%,#3a4f86)}
  .tile--chicken{left:128px;top:88px;width:124px;height:84px;background:linear-gradient(135deg,#8b6a4a,#d8b48a 50%,#4f7a2e)}
  .tile--rice{left:76px;top:36px;width:100px;height:100px;border-radius:50%;border:4px solid #fff;
              background:radial-gradient(circle,#d9c49c,#b59a6c 70%,#6e5a3c)}

  .front-title{left:0;width:284px;top:200px;font-family:"Raleway",sans-serif;font-weight:700;
               font-size:17.5px;color:var(--brick)}
  .short-rule{position:absolute;height:1.5px;width:28px;background:var(--rule)}
  .front-intro{left:14px;width:256px;top:231px;font-size:11px;line-height:12.3px}
  .band{position:absolute;left:0;width:284px;background:var(--teal);color:#fff;
        font-family:"Raleway",sans-serif;text-align:center}
  .band--steps{top:304px;height:25px;font-size:13.5px;font-weight:500;line-height:25px;letter-spacing:.1px}
  .steps{left:16px;top:339px;width:256px;list-style:none;font-size:10.5px;line-height:12.3px}
  .steps li{position:relative;padding-left:13px;margin-bottom:6px}
  .steps li::before{content:"";position:absolute;left:0;top:4.5px;width:3.5px;height:3.5px;border-radius:50%;background:var(--teal)}
  .steps li.note{margin-top:-3px}
  .steps li.note::before{display:none}
  .front-cta{left:20px;width:244px;top:578px;font-size:10.5px;line-height:13px;color:var(--brick);
             font-family:"Raleway",sans-serif;font-weight:500}
  .heritage-band{left:0;bottom:0;width:284px;height:14px;
                 background:linear-gradient(180deg,var(--teal) 0 30%,#fff 30% 40%,var(--brick) 40%)}

  /* back */
  .tab{left:81px;top:0;width:122px;height:29px;background:var(--teal);color:#fff;
       font-family:"Raleway",sans-serif;font-weight:600;font-size:12px;line-height:32px;text-align:center}
  .recipe-title{left:0;width:284px;top:36px;font-size:11px}
  .recipe-photo{left:15px;top:63px;width:90px;height:79px;background:linear-gradient(135deg,#c9c9c9,#e07a5a 45%,#6e9a3c 70%,#d0d0d0)}
  .ingredients{left:117px;top:63px;width:160px}
  .ingredients h3{font-family:"Raleway",sans-serif;font-weight:500;font-size:11px;color:var(--brick);margin-bottom:3px}
  .ingredients p{font-size:8.7px;line-height:10.8px}
  .method{left:16px;width:252px;top:156px;font-size:8.7px;line-height:10.8px}
  .quote-box{left:15px;top:242px;width:253px;height:75px;background:var(--brick);color:#fff;
             font-size:10.5px;line-height:12.2px;letter-spacing:.3px;padding:7px 14px 0;text-align:center}
  .band--info{top:331px;height:26px;font-size:13.5px;font-weight:700;line-height:27px;letter-spacing:.6px}
  .info{left:0;width:284px;top:365px;text-align:center}
  .info h4{font-size:9.5px;font-weight:700;margin-bottom:5px}
  .info .org{font-size:8.5px;font-weight:700;color:var(--brick);line-height:10px}
  .info .url{font-size:7.5px;margin-top:3px}
  .info .group{margin-bottom:10px}
  .info .tight{margin-bottom:6px}
  .long-rule{left:15px;width:254px;top:507px;height:1.5px;background:var(--rule)}
  .org-mark{left:0;width:284px;top:521px;display:flex;justify-content:center;align-items:center;gap:6px}
  .org-mark .dot{width:24px;height:24px;border-radius:50%;background:var(--teal)}
  .org-mark .name{font-family:"Raleway",sans-serif;font-weight:700;font-size:10.5px;color:var(--brick);letter-spacing:.4px}
  .funding{left:17px;width:250px;top:562px;font-size:5.4px;line-height:7px;text-align:center}
</style>
</head>
<body>

<section class="card card--front">
  <div class="abs collage">
    <div class="tile tile--salmon" role="img" aria-label="Grilled salmon fillet with cherry tomatoes on a plate"></div>
    <div class="tile tile--produce" role="img" aria-label="Assortment of fresh fruits and vegetables"></div>
    <div class="tile tile--berries" role="img" aria-label="Bowl of fresh strawberries, raspberries and blueberries"></div>
    <div class="tile tile--chicken" role="img" aria-label="Sliced grilled chicken breast with broccoli"></div>
    <div class="tile tile--rice" role="img" aria-label="Bowl of brown rice"></div>
  </div>

  <h1 class="abs front-title center">Healthy Food, Healthy Brain</h1>
  <span class="short-rule" style="left:128px;top:223px"></span>
  <p class="abs front-intro center">Everyone slows down as they get older, both in body and mind. Eating healthier food can help your overall health, including brain health. It may also reduce your risk for memory loss and problems thinking.</p>

  <h2 class="band band--steps">Healthier Steps To Protect Your Brain</h2>
  <ul class="abs steps">
    <li>Eat more vegetables, fruits, whole grains, and lower-fat milk</li>
    <li>Use less salt and added sugar</li>
    <li>Eat more fish, chicken, turkey, beans, &amp; nuts</li>
    <li>Cut down on bad fats (“saturated” &amp; trans), cholesterol, and red meat</li>
    <li>Buy fresh, not packaged food when you can</li>
    <li>Limit how much alcohol you drink</li>
    <li>Learn your daily calorie needs for your body size</li>
    <li>Take care of your mental and spiritual health to support your physical and brain health</li>
    <li class="note">Small changes can make a big difference for better brain health.</li>
  </ul>
  <span class="short-rule" style="left:128px;top:568px"></span>
  <p class="abs front-cta center">Talk to your doctor about more steps to healthier food choices</p>
  <div class="abs heritage-band" role="img" aria-label="Band of teal and red chevron pattern"></div>
</section>

<section class="card card--back">
  <div class="abs tab">Make This at Home</div>
  <h2 class="abs recipe-title center">Grilled Salmon and Veggie Foil Packets</h2>
  <div class="abs recipe-photo" role="img" aria-label="Salmon and asparagus in an open foil packet"></div>
  <div class="abs ingredients">
    <h3>Ingredients:</h3>
    <p>Salmon, Asparagus,<br>Red or Green Peppers,<br>(Or any seasonal vegetable),<br>Onion, Lemon – sliced,<br>Basil, Olive Oil, Salt &amp; Pepper,<br>Garlic Powder</p>
  </div>
  <p class="abs method center">Cut asparagus, peppers, and onion into bite-size pieces. Cut salmon into 4-6 oz pieces. Tear tin foil large enough to wrap around salmon &amp; veggies (2 layers). Add veggies and salmon to foil. Drizzle with olive oil, season with salt, pepper, basil, garlic &amp; top with a piece of sliced lemon. Wrap foil tightly around food. Grill at 400 degrees for about 20 minutes. Careful opening!</p>
  <p class="abs quote-box">Food &amp; drink are a source of strength and connection to community. A return to traditional food pathways &amp; eating local, seasonal fresh foods make healthier eating easier.</p>

  <h2 class="band band--info">FOR MORE INFORMATION</h2>
  <div class="abs info">
    <div class="group">
      <h4>About Healthier Eating</h4>
      <p class="org">PlateWise</p>
      <p class="url">https://www.platewise.org</p>
    </div>
    <div class="tight">
      <h4>About Brain Health</h4>
      <p class="org">Velmor Center for Community<br>Brain Health</p>
      <p class="url">https://www.velmorcollective.org</p>
    </div>
    <p class="org" style="margin-top:8px">Harlow Memory Health Program</p>
    <p class="url">https://www.harlowmemory.org/aging</p>
  </div>
  <div class="abs long-rule"></div>
  <div class="abs org-mark">
    <span class="dot"></span>
    <span class="name">VELMOR COLLECTIVE</span>
  </div>
  <p class="abs funding">This product is supported by the Harlow Health Agency as part of a community grant award totaling $348,711 with 100 percent funded by the agency. The contents are those of the author(s) and do not necessarily represent the official views of, nor an endorsement by, the Harlow Health Agency.</p>
  <div class="abs heritage-band" role="img" aria-label="Band of teal and red chevron pattern"></div>
</section>

</body>
</html>
```